Media Browser and player web application

I need to redesign a web application that enables to browse a media server (Lumarra) contents (images, audio, video) and play it in a web player.

Current implementation of the application can be seen at: http://www.kelbofaq.net/content/demonstration-lumarra-pro-online-media-browser

This refresh is aiming to:
1) make the application simpler, based on typology (think Panelix Tile style, VidHalo, Flickro); a simple fan concept is here: http://tow.gandeliq.net/lumarra/
2) make the application work on desktop as well as touch screen devices (ie no hover functionality, no pagination, large touch controls)
3) fast (remove unnecessary animations)
4) design with the app being responsive in mind

The attached UX designs show the basic flows in the application. Please note that the placement of controls (for example) is not set in stone and I welcome your input on the layout.

Ideally the default theme will be dark. Items' thumbnails will be square place holders, with images fit in them depending on the item icons' aspect ratio.

Also attaching the product's logo (Lumarra) and icon. The web application's name is ClipRoamer (or Lumarra ClipRoamer), so it should be included in the design (the UX designs include place holder Lumarra logo in the left top corner).

The main categories for each file type are (you will have to provide an icon for each of these):
- Audio: Albums, Artists, Album artists, Folders, Genres, Composers, Titles, Random music, Random albums, Last listened, Playlists, Online
- Image: Albums, Folders, Year, Month, Playlists, Online
- Video: Titles, Movies, Series, Folders, Last viewed, Last added, Genres, Actors, Directors, Producers, Release years, Playlists, Online
Updates

Target Market(s)

Mostly tech enthusiasts who want to stream their media over the internet to their devices.

Industry/Entity Type

Artists

Requirements
Must have
• Designs for all the provided UX designs
Touch-friendly web application design
High-res (Retina) assets
Light, type based Tile-like design
Nice to have
• Responsive web version
Dark and Light theme switching.
Should not have
• Chrome
Heavy graphics (eg backgrounds) that take time to load

```html
<!DOCTYPE html>
<html lang="en">
<head>
<meta charset="utf-8">
<title>ClipRoamer</title>
<link rel="stylesheet" href="https://fonts.googleapis.com/css2?family=Open+Sans:wght@400;700&display=swap">
<style>
  :root {
    --bg: #000000;
    --rule: #262626;
    --brand-mark: #f2e600;
    --text: #ffffff;
    --muted: #8a8a8a;
    --tile-face: #ffffff;
    --tile-label: #707070;
    --icon: #161616;
  }
  * { box-sizing: border-box; margin: 0; padding: 0; }
  html, body {
    width: 1200px; height: 644px; overflow: hidden;
    background: var(--bg);
    font-family: "Open Sans", Arial, sans-serif;
    color: var(--text);
  }
  .app { position: relative; width: 1200px; height: 644px; }
  .site-header {
    position: absolute; left: 0; top: 0; width: 100%; height: 74px;
    border-bottom: 1px dashed var(--rule);
  }
  .brand {
    position: absolute; left: 117px; top: 14px;
    display: flex; align-items: center; gap: 7px;
  }
  .brand-mark {
    width: 27px; height: 27px; border-radius: 4px; background: var(--brand-mark);
  }
  .brand-name { font-size: 33px; font-weight: 700; line-height: 46px; }
  .header-help {
    position: absolute; right: 117px; top: 28px;
    font-size: 12px; color: #d8d8d8; text-decoration: none;
  }
  .categories {
    position: absolute; left: 292px; top: 183px;
    display: flex; gap: 23px;
  }
  .category {
    width: 190px; height: 222px; border-radius: 3px; overflow: hidden;
    display: flex; flex-direction: column; text-decoration: none;
  }
  .category-face {
    height: 173px; background: var(--tile-face);
    display: flex; align-items: center; justify-content: center;
  }
  .category-face svg { width: 130px; height: 130px; }
  .category-label {
    flex: 1; background: var(--tile-label); color: var(--text);
    font-size: 23px; font-weight: 700;
    display: flex; align-items: center; justify-content: center;
  }
  .site-footer {
    position: absolute; left: 0; top: 580px; width: 100%;
    border-top: 1px dashed var(--rule);
    text-align: center; padding-top: 18px;
    font-size: 12px; color: var(--muted);
  }
  .site-footer a { color: var(--muted); text-decoration: none; }
</style>
</head>
<body>
<div class="app">
  <header class="site-header">
    <div class="brand">
      <span class="brand-mark"></span>
      <span class="brand-name">ClipRoamer</span>
    </div>
    <a class="header-help" href="#">Click Help</a>
  </header>

  <nav class="categories">
    <a class="category" href="#">
      <div class="category-face">
        <svg viewBox="0 0 130 130" aria-hidden="true">
          <g transform="translate(65 62)">
            <rect x="-55" y="-40" width="80" height="64" fill="none" stroke="var(--icon)" stroke-width="7" transform="rotate(-14)"/>
            <rect x="-27" y="-22" width="82" height="64" fill="var(--tile-face)" stroke="var(--icon)" stroke-width="7"/>
            <circle cx="-8" cy="-4" r="6" fill="var(--icon)"/>
            <polygon points="-18,32 6,12 16,22 28,6 46,32" fill="var(--icon)"/>
          </g>
        </svg>
      </div>
      <div class="category-label">Images</div>
    </a>
    <a class="category" href="#">
      <div class="category-face">
        <svg viewBox="0 0 130 130" aria-hidden="true">
          <g fill="var(--icon)">
            <polygon points="16,36 112,14 116,30 20,52"/>
            <rect x="16" y="56" width="98" height="58" rx="10"/>
          </g>
          <g fill="var(--tile-face)">
            <polygon points="32,38 44,35 38,46 26,49"/>
            <polygon points="56,32 68,29 62,40 50,43"/>
            <polygon points="80,27 92,24 86,35 74,38"/>
            <rect x="26" y="72" width="78" height="34" rx="2"/>
            <polygon points="30,58 42,58 36,66 24,66"/>
            <polygon points="56,58 68,58 62,66 50,66"/>
            <polygon points="82,58 94,58 88,66 76,66"/>
          </g>
          <polygon points="56,76 78,89 56,102" fill="var(--icon)"/>
        </svg>
      </div>
      <div class="category-label">Videos</div>
    </a>
    <a class="category" href="#">
      <div class="category-face">
        <svg viewBox="0 0 130 130" aria-hidden="true">
          <g fill="var(--icon)">
            <polygon points="38,38 104,22 104,40 46,54 46,100 38,100"/>
            <rect x="96" y="22" width="8" height="66"/>
            <ellipse cx="32" cy="100" rx="15" ry="12"/>
            <ellipse cx="90" cy="86" rx="15" ry="12"/>
          </g>
        </svg>
      </div>
      <div class="category-label">Audio</div>
    </a>
  </nav>

  <footer class="site-footer">
    Copyright 2013 - ClipRoamer &nbsp;&nbsp;- &nbsp;<a href="#">Help</a> &nbsp;- <a href="#">Terms</a>
  </footer>
</div>
</body>
</html>
```